Book Cover Design Project

We need a book cover for a eBook on internet banking.

This eBook is meant to be an easy to read, practical book to help people understand what internet banking is, the pros and cons and cover the pure 'internet only' banks that have no branches. The intention is to help people to make informed decisions about whether to use internet banking, how to use it safely and explain in detail what 'internet only' banks are and whether they are right for them.

The cover should not look technical so that non-technical people are not scared off by the look. I have uploaded a book cover design that has the style that I am trying to portray, I have also uploaded a front cover that I created but do not think is suitable.

The cover wording layout could be something like
"Internet Banking"
"A practical guide to answer all your questions" or "The ultimate guide to internet banking" or "The Who's What's and How's of Internet Banking"
Authors name : Colin Pettifer

Industry/Entity Type

Internet

```html
<!DOCTYPE html>
<html lang="en">
<head>
<meta charset="utf-8">
<title>Internet Banking – Book Cover</title>
<link rel="stylesheet" href="https://fonts.googleapis.com/css2?family=Nobile:wght@700&family=Roboto+Condensed:wght@700;800&family=Cabin:wght@500&display=swap">
<style>
  :root {
    --backdrop: #0a0a0b;
    --sky-top: #5aa6ec;
    --sky-mid: #6db3ea;
    --lime-low: #a8d42a;
    --lime-bottom: #c2dc00;
    --title-white: #ffffff;
    --subtitle-lime: #c6e000;
    --accent-blue: #1e8fe0;
    --ink: #161616;
  }
  * { margin: 0; padding: 0; box-sizing: border-box; }
  html, body {
    width: 1200px;
    height: 1000px;
    overflow: hidden;
    background: var(--backdrop);
  }
  .cover {
    position: absolute;
    left: 245px;
    top: 30px;
    width: 686px;
    height: 932px;
    overflow: hidden;
    background: linear-gradient(180deg,
      var(--sky-top) 0%,
      var(--sky-mid) 52%,
      #8cc79a 68%,
      var(--lime-low) 80%,
      var(--lime-bottom) 100%);
  }
  .light-sweep {
    position: absolute;
    left: -60px;
    top: 560px;
    width: 820px;
    height: 200px;
    background: radial-gradient(ellipse at 55% 50%, rgba(255,255,255,0.85) 0%, rgba(255,255,255,0.35) 40%, rgba(255,255,255,0) 70%);
    transform: rotate(-12deg);
  }
  .title {
    position: absolute;
    top: 24px;
    left: 0;
    width: 662px;
    text-align: center;
    font-family: "Nobile", "Verdana", sans-serif;
    font-weight: 700;
    font-size: 37px;
    color: var(--title-white);
    letter-spacing: 0.2px;
  }
  .subtitle {
    position: absolute;
    top: 80px;
    left: 0;
    width: 666px;
    text-align: center;
    font-family: "Nobile", "Verdana", sans-serif;
    font-weight: 700;
    font-size: 32px;
    line-height: 44px;
    color: var(--subtitle-lime);
    letter-spacing: 0.5px;
  }
  .hero-image {
    position: absolute;
    left: 70px;
    top: 258px;
    width: 540px;
    height: 420px;
    border-radius: 18px;
    background: linear-gradient(160deg, #8fb3c9 0%, #5e6d7a 45%, #3a3f46 70%, #9aa2a8 100%);
    opacity: 0.9;
  }
  .tagline {
    position: absolute;
    top: 718px;
    left: 0;
    width: 686px;
    text-align: center;
    font-family: "Roboto Condensed", "Arial Narrow", sans-serif;
    font-weight: 800;
    color: var(--ink);
  }
  .tagline-main {
    font-size: 38px;
    line-height: 62px;
    letter-spacing: -0.5px;
  }
  .tagline-main .key {
    color: var(--accent-blue);
    font-size: 52px;
  }
  .tagline-sub {
    font-size: 35px;
    line-height: 36px;
    padding-left: 4px;
  }
  .author {
    position: absolute;
    right: 42px;
    top: 886px;
    font-family: "Cabin", "Trebuchet MS", sans-serif;
    font-weight: 500;
    font-variant: small-caps;
    font-size: 25px;
    letter-spacing: 1.5px;
    color: var(--ink);
  }
</style>
</head>
<body>
  <main class="cover">
    <div class="light-sweep" aria-hidden="true"></div>
    <h1 class="title">Internet Banking</h1>
    <p class="subtitle">The Ultimate Guide<br>to Internet Banking</p>
    <div class="hero-image" role="img" aria-label="Photo of a laptop with a hand reaching out of the screen holding a fan of hundred-dollar banknotes"></div>
    <div class="tagline">
      <p class="tagline-main">The <span class="key">Who's</span>, <span class="key">What's</span> and <span class="key">How's</span></p>
      <p class="tagline-sub">of Internet Banking</p>
    </div>
    <p class="author">Colin Pettifer</p>
  </main>
</body>
</html>
```